Business Card Design Needed

Business car design required, logo will be supplied.

Brambleford Power Surveyors are looking to become the leading provider of energy performance certificates to estate agents, landlords and home owners in the Yorkshire region of the UK.

The business card must be double sided and professional looking. Estate agents receive hundreds of cards from contractors and our card must stand out.

I require a two sided business card that is clean, modern and created by a designer that can think outside of the box.

Brand colours can be supplied .

Please ask if you have any questions.

Target Market(s)

Estate agents, landlords and property owners

Industry/Entity Type

Property - estate agency - energy consultants

Contact Information for Business Card

Tomas Rendell - Energy Assessor - 07311642705 - www.BramblefordPSV.co.uk - info@bramblefordpsv.co.uk

Font styles to use
Serif
Sans Serif

Colors
00AB8E
00BBA5
67D7C9
C6EFE9
E9F9F6

Requirements
Must have
• Use the provided logo, clean, professional and stand out from the crowd
Nice to have
• Clever use of text, spacing and brand colours
Should not have
• Clip art

```html
<!DOCTYPE html>
<html lang="en">
<head>
<meta charset="utf-8">
<title>Brambleford Power Surveyors – Business Card</title>
<link rel="stylesheet" href="https://fonts.googleapis.com/css2?family=Roboto:wght@400;500;700&display=swap">
<style>
  :root {
    --page-bg: #9a9a9a;
    --brand-blue: #0067a3;
    --brand-lime: #b8cf17;
    --brand-cyan: #12e6ff;
    --brand-navy: #03105a;
    --paper: #ffffff;
    --paper-tint: #e6eff5;
    --text-light: #ffffff;
  }
  * { margin: 0; padding: 0; box-sizing: border-box; }
  html, body {
    width: 1133px;
    height: 1200px;
    overflow: hidden;
    background: var(--page-bg);
    font-family: "Roboto", Arial, sans-serif;
  }
  .card {
    position: absolute;
    left: 200px;
    width: 733px;
    height: 418px;
    border-radius: 22px;
    overflow: hidden;
    background: var(--brand-blue);
  }
  .card--front { top: 138px; }
  .card--back { top: 640px; }

  .card__art {
    position: absolute;
    inset: 0;
    width: 100%;
    height: 100%;
  }

  .contact {
    position: absolute;
    left: 38px;
    top: 144px;
    color: var(--text-light);
  }
  .contact__name {
    font-size: 25px;
    font-weight: 700;
    color: var(--brand-lime);
    line-height: 1;
  }
  .contact__role {
    margin-top: 9px;
    font-size: 16px;
    font-weight: 500;
    line-height: 1;
  }
  .contact__list {
    list-style: none;
    margin-top: 20px;
  }
  .contact__item {
    display: flex;
    align-items: center;
    gap: 9px;
    font-size: 16.5px;
    line-height: 21px;
  }
  .contact__icon {
    width: 13px;
    height: 13px;
    flex: none;
  }

  .brand-mark {
    position: absolute;
    left: 372px;
    top: 182px;
    display: flex;
    align-items: center;
    gap: 10px;
  }
  .brand-mark__dot {
    width: 30px;
    height: 30px;
    border-radius: 50%;
    background: var(--brand-lime);
    flex: none;
  }
  .brand-mark__name {
    font-size: 21px;
    font-weight: 400;
    color: var(--brand-blue);
    white-space: nowrap;
  }

  .back-brand {
    position: absolute;
    right: 48px;
    bottom: 34px;
    text-align: right;
    color: var(--text-light);
  }
  .back-brand__name {
    font-size: 30px;
    font-weight: 400;
    line-height: 1.08;
  }
  .back-brand__web {
    margin-top: 10px;
    font-size: 16px;
    letter-spacing: 1.3px;
  }
</style>
</head>
<body>

<section class="card card--front" aria-label="Business card front">
  <svg class="card__art" viewBox="0 0 733 418" aria-hidden="true">
    <defs>
      <radialGradient id="paperGlow" cx="0.62" cy="0.5" r="0.6">
        <stop offset="0.7" stop-color="var(--paper)"/>
        <stop offset="1" stop-color="var(--paper-tint)"/>
      </radialGradient>
    </defs>
    <path d="M489 0 C340 28 300 110 300 209 C300 308 340 390 489 418 L733 418 L733 0 Z" fill="var(--brand-lime)"/>
    <path d="M497 0 C350 28 309 110 309 209 C309 308 350 390 497 418 L733 418 L733 0 Z" fill="url(#paperGlow)"/>
  </svg>

  <div class="contact">
    <h1 class="contact__name">TOMAS RENDELL</h1>
    <p class="contact__role">Energy Assessor</p>
    <ul class="contact__list">
      <li class="contact__item">
        <svg class="contact__icon" viewBox="0 0 16 16" aria-hidden="true"><path d="M3.5 1.5 L6 1 L7.3 4.6 L5.6 5.8 C6.4 7.7 8.3 9.6 10.2 10.4 L11.4 8.7 L15 10 L14.5 12.5 C14.2 13.8 13 14.6 11.7 14.4 C6.5 13.5 2.5 9.5 1.6 4.3 C1.4 3 2.2 1.8 3.5 1.5 Z" fill="var(--brand-lime)"/></svg>
        <span>07311642705</span>
      </li>
      <li class="contact__item">
        <svg class="contact__icon" viewBox="0 0 16 16" aria-hidden="true"><rect x="1" y="4" width="14" height="9" fill="var(--brand-lime)"/><path d="M1 4 L8 9 L15 4" fill="none" stroke="var(--brand-blue)" stroke-width="1.2"/></svg>
        <span>info@bramblefordpsv.co.uk</span>
      </li>
      <li class="contact__item">
        <svg class="contact__icon" viewBox="0 0 16 16" aria-hidden="true"><circle cx="8" cy="8" r="7" fill="var(--brand-lime)"/><path d="M8 1 V15 M1 8 H15 M3 4.5 H13 M3 11.5 H13" stroke="var(--brand-blue)" stroke-width="1"/></svg>
        <span>www.BramblefordPSV.co.uk</span>
      </li>
    </ul>
  </div>

  <div class="brand-mark">
    <span class="brand-mark__dot" aria-hidden="true"></span>
    <span class="brand-mark__name">Brambleford Power Surveyors</span>
  </div>
</section>

<section class="card card--back" aria-label="Business card back">
  <svg class="card__art" viewBox="0 0 733 418" role="img" aria-label="Large brand emblem area in cyan-to-navy tones">
    <defs>
      <linearGradient id="emblemTone" x1="0" y1="0" x2="1" y2="0">
        <stop offset="0" stop-color="var(--brand-cyan)"/>
        <stop offset="0.45" stop-color="#0a6fd6"/>
        <stop offset="1" stop-color="var(--brand-navy)"/>
      </linearGradient>
    </defs>
    <circle cx="214" cy="209" r="205" fill="url(#emblemTone)"/>
  </svg>

  <div class="back-brand">
    <p class="back-brand__name">Brambleford<br>Power Surveyors</p>
    <p class="back-brand__web">www.BramblefordPSV.co.uk</p>
  </div>
</section>

</body>
</html>
```